Label for a new Bourbon bottle

Name of the new Bourbon is Corvena. This will be a Straight Bourbon Finished in Sherry Casks. We are calling in Corvena to give it the look and feel of Spanish and Portuguese influence where sherry comes from. I've included some samples of labels in the US, you can also take a look at Spanish sherry bottle labels included too and get some inspiration, it can have traditional influence but with it's own style, not too focused on barrels. The proof will be 90, alc. by vol. 45%. Volume 750 ML.

Target Market(s)

Whiskey and Bourbon drinkers

Requirements
Must have
• Elegant, classy but not a mirror of what so many traditional labels look like, must feel high-end, expensive

```html
<!DOCTYPE html>
<html lang="en">
<head>
<meta charset="utf-8">
<title>Corvena Straight Bourbon Whiskey Label</title>
<link href="https://fonts.googleapis.com/css2?family=Playfair+Display+SC:wght@700;900&family=Cormorant+Garamond:wght@500;600;700&family=Pinyon+Script&display=swap" rel="stylesheet">
<style>
  :root {
    --backdrop: #e9e8e6;
    --label-paper: #fbf8f3;
    --ink: #2f2520;
    --accent-red: #b3402a;
    --band-brown: #6b3a20;
    --band-text: #f6ead8;
    --band-rule: #c9a27a;
    --art-grey: #9a9794;
  }
  * { margin: 0; padding: 0; box-sizing: border-box; }
  html, body {
    width: 964px; height: 1200px; overflow: hidden;
    background: var(--backdrop);
  }
  .canvas {
    width: 964px; height: 1200px;
    display: flex; align-items: center; justify-content: center;
  }
  .label {
    position: relative;
    width: 620px; height: 1040px;
    background: var(--label-paper);
    box-shadow: 0 2px 10px rgba(0,0,0,0.08);
    display: flex; flex-direction: column; align-items: center;
    color: var(--ink);
    font-family: "Cormorant Garamond", serif;
  }
  .heritage {
    margin-top: 44px;
    display: flex; align-items: center; gap: 26px;
    font-family: "Pinyon Script", cursive;
    font-size: 26px; color: var(--ink);
  }
  .heritage-emblem {
    width: 96px; height: 62px;
    border-radius: 4px;
    background: linear-gradient(180deg, #cfcac4, #a7a19b);
  }
  .brand-name {
    margin-top: 26px;
    font-family: "Playfair Display SC", serif;
    font-weight: 900;
    font-size: 96px;
    letter-spacing: 12px;
    color: var(--accent-red);
    line-height: 1;
    padding-left: 12px;
  }
  .spirit-type {
    margin-top: 18px;
    text-align: center;
    font-weight: 600;
    font-size: 25px;
    letter-spacing: 3px;
    line-height: 1.15;
    text-transform: uppercase;
  }
  .hero-art {
    margin-top: 26px;
    width: 520px; height: 380px;
    background:
      radial-gradient(ellipse at 62% 45%, rgba(179,64,42,0.85) 0%, rgba(179,64,42,0.55) 38%, rgba(179,64,42,0) 62%),
      linear-gradient(135deg, #d8d4cf 0%, var(--art-grey) 55%, #4a4542 100%);
    border-radius: 3px;
  }
  .finish-line {
    margin-top: 34px;
    font-weight: 600;
    font-size: 22px;
    letter-spacing: 3px;
    color: var(--accent-red);
    text-transform: uppercase;
  }
  .finish-cask {
    margin-top: 2px;
    font-family: "Pinyon Script", cursive;
    font-size: 60px;
    color: var(--accent-red);
    line-height: 1.1;
  }
  .origin {
    margin-top: 10px;
    font-weight: 700;
    font-size: 21px;
    letter-spacing: 2px;
    text-transform: uppercase;
  }
  .spec-band {
    position: absolute; left: 0; right: 0; bottom: 0;
    height: 110px;
    background: var(--band-brown);
    display: flex; align-items: center; justify-content: center;
    gap: 0;
    color: var(--band-text);
  }
  .spec-mark {
    width: 40px; height: 40px;
    background: #e0883c;
    margin-right: 34px;
  }
  .spec-item {
    display: flex; flex-direction: column; align-items: center;
    padding: 0 30px;
    line-height: 1;
  }
  .spec-item + .spec-item { border-left: 2px solid var(--band-rule); }
  .spec-value {
    font-family: "Playfair Display SC", serif;
    font-weight: 700;
    font-size: 38px;
  }
  .spec-unit {
    margin-top: 6px;
    font-weight: 700;
    font-size: 15px;
    letter-spacing: 2px;
  }
</style>
</head>
<body>
  <main class="canvas">
    <section class="label">
      <div class="heritage">
        <span class="heritage-year">Estd.</span>
        <div class="heritage-emblem" role="img" aria-label="Small engraved illustration of a country estate"></div>
        <span class="heritage-year">2020</span>
      </div>

      <h1 class="brand-name">CORVENA</h1>
      <p class="spirit-type">Straight Bourbon<br>Whiskey</p>

      <div class="hero-art" role="img" aria-label="Engraved illustration of a matador with cape and a charging bull over a large red initial"></div>

      <p class="finish-line">Finished in</p>
      <p class="finish-cask">Sherry Casks</p>
      <p class="origin">Product of Spain</p>

      <div class="spec-band">
        <div class="spec-mark"></div>
        <div class="spec-item"><span class="spec-value">90</span><span class="spec-unit">PROOF</span></div>
        <div class="spec-item"><span class="spec-value">45%</span><span class="spec-unit">ALC/VOL</span></div>
        <div class="spec-item"><span class="spec-value">750</span><span class="spec-unit">ML</span></div>
      </div>
    </section>
  </main>
</body>
</html>
```